Business Card Design

We need a business card for a new business based in Sydney, Australia. It is a home based baking business, the key products are cookies and muffins and slices including gluten free baked goods. With the emphasis on home made baking. The target market is cafes, coffee shops and vans, restaurants. Products may be provided in display jars or individually wrapped. The final design should be in the colours pink, purple.

Industry/Entity Type

Business

Contact Information for Business Card

Pindle's Bakery Pty Ltd, Maren Tulloch, maren@pindlesbakery.com.au
0412 506 218, www.pindlesbakery.com.au, ACN 581 246 037,

```html
<!DOCTYPE html>
<html lang="en">
<head>
<meta charset="utf-8">
<title>Pindle's Bakery – Business Card</title>
<link href="https://fonts.googleapis.com/css2?family=Cinzel:wght@400;700&display=swap" rel="stylesheet">
<style>
  :root {
    --backdrop: #e9e6ec;
    --card-white: #ffffff;
    --pink-deep: #e8487f;
    --pink-soft: #f4a3c0;
    --purple-band: #8677bb;
    --purple-light: #b1a6d8;
    --purple-brand: #6c2a9e;
    --text-light: #ffffff;
  }
  * { margin: 0; padding: 0; box-sizing: border-box; }
  html, body {
    width: 1200px; height: 901px; overflow: hidden;
    background: var(--backdrop);
  }
  .canvas {
    width: 1200px; height: 901px;
    display: flex; align-items: center; justify-content: center;
  }
  .business-card {
    position: relative;
    width: 1000px; height: 572px;
    border-radius: 56px;
    overflow: hidden;
    background: var(--card-white);
    box-shadow: 0 10px 30px rgba(60, 40, 80, 0.18);
    font-family: 'Cinzel', serif;
  }
  .card-waves { position: absolute; inset: 0; width: 100%; height: 100%; }
  .brand {
    position: absolute; left: 430px; top: 120px;
    display: flex; align-items: center; gap: 18px;
  }
  .brand-dot {
    width: 64px; height: 64px; border-radius: 50%;
    background: var(--pink-deep);
  }
  .brand-name {
    font-family: 'Cinzel', serif;
    font-weight: 700; font-size: 40px;
    color: var(--purple-brand);
    letter-spacing: 0.5px;
  }
  .contact-list {
    position: absolute; left: 48px; top: 196px;
    list-style: none;
    color: var(--text-light);
    font-size: 17px; line-height: 25px;
    letter-spacing: 0.4px;
  }
  .contact-list li { display: flex; align-items: flex-start; gap: 10px; }
  .contact-icon { flex: 0 0 16px; width: 16px; height: 16px; margin-top: 4px; }
  .contact-indent { padding-left: 26px; }
  .cardholder {
    position: absolute; right: 70px; bottom: 46px;
    text-align: right; color: var(--text-light);
    font-size: 26px; line-height: 32px; letter-spacing: 1px;
  }
  .cardholder-name { display: block; }
  .cardholder-role { display: block; font-size: 23px; }
</style>
</head>
<body>
<main class="canvas">
  <section class="business-card" aria-label="Pindle's Bakery business card">
    <svg class="card-waves" viewBox="0 0 1000 572" preserveAspectRatio="none" aria-hidden="true">
      <defs>
        <linearGradient id="bandPurple" x1="0" y1="0" x2="1" y2="0">
          <stop offset="0" stop-color="var(--purple-band)"/>
          <stop offset="1" stop-color="var(--purple-light)"/>
        </linearGradient>
        <linearGradient id="bodyPink" x1="0" y1="0" x2="1" y2="1">
          <stop offset="0" stop-color="var(--pink-deep)"/>
          <stop offset="1" stop-color="var(--pink-soft)"/>
        </linearGradient>
      </defs>
      <path d="M0,40 C240,120 470,320 1000,300 L1000,572 L0,572 Z" fill="url(#bandPurple)"/>
      <path d="M0,76 C240,156 470,356 1000,336 L1000,572 L0,572 Z" fill="var(--pink-deep)"/>
      <path d="M0,84 C240,164 470,364 1000,344 L1000,572 L0,572 Z" fill="url(#bandPurple)"/>
      <path d="M0,92 C240,172 470,372 1000,352 L1000,572 L0,572 Z" fill="url(#bodyPink)"/>
    </svg>

    <div class="brand">
      <span class="brand-dot"></span>
      <span class="brand-name">Pindle's Bakery</span>
    </div>

    <ul class="contact-list">
      <li>
        <svg class="contact-icon" viewBox="0 0 16 16"><circle cx="8" cy="8" r="8" fill="#fff"/><path d="M8 3.5a3 3 0 0 0-3 3c0 2.2 3 5.8 3 5.8s3-3.6 3-5.8a3 3 0 0 0-3-3z" fill="var(--pink-deep)"/></svg>
        <span>Suite 4, 18 Larkin St,</span>
      </li>
      <li class="contact-indent">Sydney NSW 2000</li>
      <li>
        <svg class="contact-icon" viewBox="0 0 16 16"><circle cx="8" cy="8" r="8" fill="#fff"/><path d="M5.5 4h2l.6 2-1.2.8a5 5 0 0 0 2.3 2.3l.8-1.2 2 .6v2c0 .5-.5 1-1 1A6.5 6.5 0 0 1 4.5 5c0-.5.5-1 1-1z" fill="var(--pink-deep)"/></svg>
        <span>0412 506 218</span>
      </li>
      <li>
        <svg class="contact-icon" viewBox="0 0 16 16"><circle cx="8" cy="8" r="8" fill="#fff"/><path d="M5.5 4h2l.6 2-1.2.8a5 5 0 0 0 2.3 2.3l.8-1.2 2 .6v2c0 .5-.5 1-1 1A6.5 6.5 0 0 1 4.5 5c0-.5.5-1 1-1z" fill="var(--pink-deep)"/></svg>
        <span>02 9184 3370</span>
      </li>
      <li>
        <svg class="contact-icon" viewBox="0 0 16 16"><circle cx="8" cy="8" r="8" fill="#fff"/><path d="M5.5 4h2l.6 2-1.2.8a5 5 0 0 0 2.3 2.3l.8-1.2 2 .6v2c0 .5-.5 1-1 1A6.5 6.5 0 0 1 4.5 5c0-.5.5-1 1-1z" fill="var(--pink-deep)"/></svg>
        <span>02 9184 3371</span>
      </li>
      <li>
        <svg class="contact-icon" viewBox="0 0 16 16"><circle cx="8" cy="8" r="8" fill="#fff"/><rect x="4" y="5" width="8" height="6" rx="1" fill="var(--pink-deep)"/><path d="M4.3 5.4 8 8.3l3.7-2.9" stroke="#fff" stroke-width="0.9" fill="none"/></svg>
        <span>maren@pindlesbakery.com.au</span>
      </li>
      <li>
        <svg class="contact-icon" viewBox="0 0 16 16"><circle cx="8" cy="8" r="8" fill="#fff"/><circle cx="8" cy="8" r="4" fill="none" stroke="var(--pink-deep)" stroke-width="1.2"/><path d="M4 8h8M8 4c-1.6 2.4-1.6 5.6 0 8M8 4c1.6 2.4 1.6 5.6 0 8" stroke="var(--pink-deep)" stroke-width="0.9" fill="none"/></svg>
        <span>www.pindlesbakery.com.au</span>
      </li>
    </ul>

    <div class="cardholder">
      <span class="cardholder-name">Maren Tulloch</span>
      <span class="cardholder-role">Owner / C.E.O</span>
    </div>
  </section>
</main>
</body>
</html>
```